Drinks Menu for Entertainment Venue

Need a drinks menu that is easier for an older demographic who can't use QR codes.
These are all the costs and information we need on it.
I made this within an hour on canva but as we are a world class venue I need his revamped, more professional and beautifully presented.
Pink are the main colours.
No pictures needed.
3 fold is also not required if there is a better design.

Target Market(s)

45-60

Industry/Entity Type

Entertainment and Hospitality

Colors
E54698
E96AAD
F1A4CE
F9D9EA
FCEFF6

Requirements
Must have
• Colour, easy to ready

```html
<!DOCTYPE html>
<html lang="en">
<head>
<meta charset="utf-8">
<title>Rosella – Drinks Menu</title>
<link rel="stylesheet" href="https://fonts.googleapis.com/css2?family=Playfair+Display:wght@600;700&family=Lato:wght@400;700&display=swap">
<style>
:root{
  --pink:#e54698;
  --pink-mid:#e96aad;
  --pink-soft:#f1a4ce;
  --blush:#f9d9ea;
  --mist:#fcefF6;
  --white:#ffffff;
  --ink:#5a2a43;
  --stage:#eee5df;
}
*{box-sizing:border-box;margin:0;padding:0}
html,body{width:904px;height:1200px;overflow:hidden;background:var(--stage)}
body{font-family:'Lato',sans-serif;color:var(--ink)}
.sheet{position:absolute;left:17px;width:870px;height:570px;display:flex;box-shadow:0 4px 14px rgba(90,42,67,.18)}
.sheet--outside{top:20px}
.sheet--inside{top:610px}
.panel{width:290px;height:100%;position:relative;padding:16px 16px 0;display:flex;flex-direction:column;overflow:hidden}
.panel--pink{background:var(--pink);color:var(--white)}
.panel--white{background:var(--white);color:var(--ink)}
.panel + .panel{border-left:1px solid rgba(0,0,0,.08)}

.band{position:relative;height:22px;margin:10px 0 7px;display:flex;align-items:center;justify-content:center;
  font-family:'Playfair Display',serif;font-weight:600;font-size:10.5px;letter-spacing:1.2px;text-transform:uppercase}
.band::before,.band::after{content:"";position:absolute;top:0;bottom:0;width:22px;
  background:repeating-linear-gradient(90deg,currentColor 0 2px,transparent 2px 5px)}
.band::before{left:0}.band::after{right:0}
.panel--white .band{background:var(--pink);color:var(--white)}
.panel--white .band::before,.panel--white .band::after{background:repeating-linear-gradient(90deg,var(--white) 0 2px,var(--pink) 2px 5px)}
.panel--pink .band{background:var(--white);color:var(--pink)}
.panel--pink .band::before,.panel--pink .band::after{background:repeating-linear-gradient(90deg,var(--pink) 0 2px,var(--white) 2px 5px)}
.band:first-child{margin-top:0}

.sub{font-family:'Playfair Display',serif;font-size:9.5px;font-weight:700;letter-spacing:1px;text-transform:uppercase;
  padding:3px 6px;margin:7px 0 4px;background:var(--pink-mid);color:var(--white)}
.list{list-style:none}
.item{display:flex;justify-content:space-between;font-size:10px;line-height:1.55;padding:0 4px}
.item .price{font-weight:700}
.panel--white .item{border-bottom:1px dotted var(--pink-soft)}
.panel--pink .item{border-bottom:1px dotted rgba(255,255,255,.35)}
.list--spirits .item{line-height:1.78}

.cocktail{padding:3px 4px 5px;border-bottom:1px dotted var(--pink-soft)}
.cocktail .item{border:0;padding:0;font-weight:700;color:var(--pink)}
.cocktail p{font-size:8.5px;line-height:1.35;color:var(--ink)}
.panel--blush{background:var(--mist)}

.photo{position:absolute;left:0;right:0;bottom:0}
.photo--cocktails{height:70px;background:linear-gradient(90deg,#7a1f4c,#e96aad 30%,#f6c14d 50%,#7fc46b 70%,#b53a7c)}
.photo--glasses{height:64px;background:linear-gradient(180deg,var(--white),#f4c7dd 60%,#e96aad)}
.photo--flames{height:130px;background:linear-gradient(180deg,var(--pink) 0%,#9b3fb8 45%,#f08a4b 75%,#3b2a6b)}
.photo--layered{position:absolute;left:40px;top:150px;width:210px;height:170px;border-radius:6px;
  background:linear-gradient(180deg,#f3d6e6 0%,#e54698 30%,#f6a03c 55%,#f6d64c 72%,#7b3f9e 100%)}
.tag{position:absolute;right:58px;bottom:16px;width:22px;height:26px;background:var(--white)}

.brand{display:flex;align-items:center;justify-content:center;gap:8px;margin-top:30px}
.brand .dot{width:16px;height:16px;border-radius:50%;background:var(--pink)}
.brand .name{font-family:'Playfair Display',serif;font-weight:700;font-size:28px;color:var(--pink);letter-spacing:1px}
.title{position:absolute;left:62px;right:62px;top:370px;padding:16px 0;border:2px dashed var(--pink);text-align:center;
  font-family:'Playfair Display',serif;font-weight:700;color:var(--pink);line-height:1}
.title span{display:block;font-size:30px;letter-spacing:3px}
.title span + span{font-size:40px;margin-top:4px}
</style>
</head>
<body>

<section class="sheet sheet--outside">
  <div class="panel panel--white">
    <div class="band">White Wine – Bottle</div>
    <ul class="list">
      <li class="item"><span>Pinot Grigio, Veneto</span><span class="price">£24.00</span></li>
      <li class="item"><span>Sauvignon Blanc, Marlborough</span><span class="price">£28.00</span></li>
      <li class="item"><span>Chenin Blanc, Stellenbosch</span><span class="price">£26.00</span></li>
    </ul>
    <div class="band">Rosé Wine – Bottle</div>
    <ul class="list">
      <li class="item"><span>Provence Rosé</span><span class="price">£27.00</span></li>
    </ul>
    <div class="band">Red Wine – Bottle</div>
    <ul class="list">
      <li class="item"><span>Malbec, Mendoza</span><span class="price">£28.00</span></li>
      <li class="item"><span>Merlot, Central Valley</span><span class="price">£25.00</span></li>
    </ul>
    <div class="band">Champagne</div>
    <ul class="list">
      <li class="item"><span>Brut Reserve</span><span class="price">£65.00</span></li>
      <li class="item"><span>Rosé Champagne</span><span class="price">£80.00</span></li>
      <li class="item"><span>Vintage Cuvée</span><span class="price">£95.00</span></li>
    </ul>
    <div class="band">Sparkling Wine</div>
    <ul class="list">
      <li class="item"><span>Prosecco DOC</span><span class="price">£30.00</span></li>
    </ul>
    <div class="photo photo--cocktails" role="img" aria-label="Row of colourful cocktails in glasses"></div>
  </div>

  <div class="panel panel--pink">
    <div class="band">Spirits</div>
    <ul class="list list--spirits">
      <li class="item"><span>House Vodka</span><span class="price">£5.00</span></li>
      <li class="item"><span>Premium Vodka</span><span class="price">£6.50</span></li>
      <li class="item"><span>London Dry Gin</span><span class="price">£5.50</span></li>
      <li class="item"><span>Pink Gin</span><span class="price">£6.00</span></li>
      <li class="item"><span>Botanical Gin</span><span class="price">£6.50</span></li>
      <li class="item"><span>White Rum</span><span class="price">£5.00</span></li>
      <li class="item"><span>Spiced Rum</span><span class="price">£5.50</span></li>
      <li class="item"><span>Dark Rum</span><span class="price">£5.50</span></li>
      <li class="item"><span>Silver Tequila</span><span class="price">£5.50</span></li>
      <li class="item"><span>Gold Tequila</span><span class="price">£6.00</span></li>
      <li class="item"><span>Blended Scotch</span><span class="price">£5.50</span></li>
      <li class="item"><span>Single Malt</span><span class="price">£8.00</span></li>
      <li class="item"><span>Irish Whiskey</span><span class="price">£6.00</span></li>
      <li class="item"><span>Bourbon</span><span class="price">£6.00</span></li>
      <li class="item"><span>Cognac VS</span><span class="price">£7.00</span></li>
      <li class="item"><span>Cognac XO</span><span class="price">£12.00</span></li>
      <li class="item"><span>Amaretto</span><span class="price">£5.00</span></li>
      <li class="item"><span>Sambuca</span><span class="price">£4.50</span></li>
      <li class="item"><span>Coffee Liqueur</span><span class="price">£5.00</span></li>
      <li class="item"><span>Cream Liqueur</span><span class="price">£5.00</span></li>
    </ul>
    <div class="tag"></div>
  </div>

  <div class="panel panel--white">
    <div class="brand"><span class="dot"></span><span class="name">Rosella</span></div>
    <div class="photo--layered" role="img" aria-label="Layered rainbow cocktails garnished with strawberries"></div>
    <h1 class="title"><span>Drinks</span><span>Menu</span></h1>
  </div>
</section>

<section class="sheet sheet--inside">
  <div class="panel panel--pink">
    <div class="band">Soft Drinks</div>
    <div class="sub">Soft Drinks</div>
    <ul class="list">
      <li class="item"><span>Cola</span><span class="price">£3.00</span></li>
      <li class="item"><span>Diet Cola</span><span class="price">£3.00</span></li>
      <li class="item"><span>Lemonade</span><span class="price">£3.00</span></li>
      <li class="item"><span>Orange Juice</span><span class="price">£3.50</span></li>
      <li class="item"><span>Cranberry Juice</span><span class="price">£3.50</span></li>
    </ul>
    <div class="sub">Hot Drinks</div>
    <ul class="list">
      <li class="item"><span>Americano</span><span class="price">£3.00</span></li>
      <li class="item"><span>Latte</span><span class="price">£3.50</span></li>
      <li class="item"><span>Cappuccino</span><span class="price">£3.50</span></li>
      <li class="item"><span>English Tea</span><span class="price">£2.50</span></li>
    </ul>
    <div class="sub">Mocktails</div>
    <ul class="list">
      <li class="item"><span>Virgin Mojito</span><span class="price">£6.00</span></li>
      <li class="item"><span>Berry Fizz</span><span class="price">£6.00</span></li>
    </ul>
    <div class="sub">Water</div>
    <ul class="list">
      <li class="item"><span>Still Water</span><span class="price">£2.50</span></li>
      <li class="item"><span>Sparkling Water</span><span class="price">£2.50</span></li>
    </ul>
    <div class="photo photo--cocktails" role="img" aria-label="Colourful mojitos and cocktails"></div>
  </div>

  <div class="panel panel--white panel--blush">
    <div class="band">Signature Cocktails</div>
    <div class="cocktail"><div class="item"><span>Rose Garden Spritz</span><span class="price">£12.00</span></div><p>Gin, rose syrup, prosecco and soda.</p></div>
    <div class="cocktail"><div class="item"><span>Passion Star Martini</span><span class="price">£12.00</span></div><p>Vanilla vodka, passion fruit, prosecco shot.</p></div>
    <div class="cocktail"><div class="item"><span>Berry Mojito</span><span class="price">£11.00</span></div><p>White rum, mint, lime and mixed berries.</p></div>
    <div class="cocktail"><div class="item"><span>Espresso Martini</span><span class="price">£12.00</span></div><p>Vodka, coffee liqueur and fresh espresso.</p></div>
    <div class="cocktail"><div class="item"><span>Strawberry Daiquiri</span><span class="price">£11.00</span></div><p>Rum, strawberries, lime, blended with ice.</p></div>
    <div class="cocktail"><div class="item"><span>Sunset Paloma</span><span class="price">£11.00</span></div><p>Tequila, pink grapefruit, lime and soda.</p></div>
    <div class="cocktail"><div class="item"><span>Classic Cosmopolitan</span><span class="price">£11.00</span></div><p>Citrus vodka, triple sec, cranberry, lime.</p></div>
    <div class="cocktail"><div class="item"><span>Peach Bellini</span><span class="price">£10.00</span></div><p>Prosecco topped with white peach purée.</p></div>
    <div class="photo photo--glasses" role="img" aria-label="Row of cocktail glasses"></div>
  </div>

  <div class="panel panel--pink">
    <div class="band">Beers</div>
    <ul class="list">
      <li class="item"><span>Pale Lager</span><span class="price">£5.50</span></li>
      <li class="item"><span>Craft IPA</span><span class="price">£6.00</span></li>
      <li class="item"><span>Apple Cider</span><span class="price">£5.50</span></li>
      <li class="item"><span>Irish Stout</span><span class="price">£6.00</span></li>
    </ul>
    <div class="band">Wine on Tap</div>
    <ul class="list">
      <li class="item"><span>House White</span><span class="price">£6.50</span></li>
      <li class="item"><span>House Red</span><span class="price">£6.50</span></li>
      <li class="item"><span>House Rosé</span><span class="price">£6.50</span></li>
    </ul>
    <div class="band">Shots</div>
    <ul class="list">
      <li class="item"><span>Tequila Slammer</span><span class="price">£4.00</span></li>
      <li class="item"><span>Sambuca</span><span class="price">£4.00</span></li>
      <li class="item"><span>Berry Bomb</span><span class="price">£5.00</span></li>
      <li class="item"><span>Layered B-52</span><span class="price">£5.00</span></li>
    </ul>
    <div class="photo photo--flames" role="img" aria-label="Flaming shots lined up on a bar"></div>
  </div>
</section>

</body>
</html>
```